Rising Paths Web Design

I am starting a new company that will provide LIFE COACHING services - I have tried to design a website, but it's too complicated. Right now, it's just me - I'm the only person that will provide services through the website - I have used artmarket to purchase a logo (see below). I want to be able to update the website myself, but need a template - basic design. Because I am not technologically savvy enough to explain in words - I basically want to have a website that will provide basic information about my services (coaching), a page about me and my background, hopefully scheduling possibilities, and testimonials — also a page for writing/blogs. I bought a website through NetHarbor - so when I have a template, I guess I”d use that - but maybe I’ll need to work with a designer to actually get it up on the internet. I have a head shot that I’ll upload, too.
Target Market(s)
Clients from the independent (private school) world - teachers, administrators
Number of Pages Required
4 page
Look and feel
Each slider illustrates characteristics of the customer's brand and the style your logo design should communicate.

```html
<!DOCTYPE html>
<html lang="en">
<head>
<meta charset="utf-8">
<title>Rising Paths Coaching</title>
<link rel="stylesheet" href="https://fonts.googleapis.com/css2?family=Cinzel:wght@400;500&family=Montserrat:wght@400;500;600&display=swap">
<style>
:root{
  --teal:#00a596;
  --ink:#222;
  --muted:#777;
  --soft:#f7f7f7;
  --footer:#3e3e40;
  --white:#fff;
}
*{margin:0;padding:0;box-sizing:border-box}
html,body{width:1200px;height:4354px;overflow:hidden}
body{position:relative;background:var(--white);font-family:'Montserrat',sans-serif;color:var(--ink)}
.abs{position:absolute}
.kicker{font-size:25px;color:var(--teal);font-weight:400}
.section-title{font-family:'Cinzel',serif;font-size:42px;letter-spacing:1px;color:var(--ink)}
.center{text-align:center;left:0;width:1200px}

/* header */
.site-header{top:0;left:0;width:1200px;height:123px;background:var(--white);z-index:5}
.brand{left:110px;top:6px;width:180px;height:180px;border-radius:50%;border:3px solid var(--teal);background:var(--white);display:flex;align-items:center;justify-content:center;z-index:6}
.brand span{font-family:'Cinzel',serif;font-size:23px;color:#444;text-align:center;line-height:1.15}
.nav{right:110px;top:52px;display:flex;gap:25px;font-family:'Cinzel',serif;font-size:17px;color:#333}
.nav .active{color:var(--teal)}

/* hero */
.hero{top:123px;left:0;width:1200px;height:722px;overflow:hidden}
.hero-photo{position:absolute;inset:0;background:linear-gradient(100deg,#2b2418 0%,#6b5b3d 30%,#b49a66 55%,#d8c79e 75%,#eee8d8 100%)}
.hero-sub{left:110px;top:188px;font-size:31px;color:var(--white)}
.hero-title{left:110px;top:244px;font-family:'Cinzel',serif;font-size:58px;color:var(--white);letter-spacing:1px}
.btn-outline{left:110px;top:359px;width:350px;height:67px;border:2px solid var(--white);border-radius:34px;color:var(--white);font-size:18px;font-weight:500;display:flex;align-items:center;justify-content:center;letter-spacing:.5px}
.hero-wave{position:absolute;left:0;top:0}

/* about */
.about-frame{left:122px;top:930px;width:380px;height:440px;background:#e3eeed;transform:rotate(-3deg)}
.about-frame2{left:190px;top:920px;width:380px;height:460px;background:#ececec;transform:rotate(2deg)}
.about-photo{left:193px;top:948px;width:375px;height:412px;background:linear-gradient(135deg,#2f3a3f,#6e7c82 50%,#c9c4bb);box-shadow:0 4px 10px rgba(0,0,0,.25)}
.about-text{left:653px;top:950px;width:440px}
.about-text .kicker{font-size:24px}
.about-name{font-family:'Cinzel',serif;font-size:42px;margin-top:8px}
.about-text p{margin-top:22px;font-size:15.5px;line-height:28px;color:var(--muted)}
.signature{left:640px;top:1226px;width:330px;height:78px;background:linear-gradient(90deg,#f1f1f1,#e6e6e6)}

/* services */
.services{top:1457px;left:0;width:1200px;height:647px;background:var(--soft)}
.service{top:180px;width:240px;text-align:center}
.service-ring{width:212px;height:212px;margin:0 auto;border-radius:50%;border:2px solid var(--teal);position:relative;background:var(--white)}
.service-ring::after{content:"";position:absolute;inset:4px;border-radius:50%;border:1px solid #9ed8d2}
.service-icon{position:absolute;left:56px;top:56px;width:100px;height:100px;border-radius:50%;background:#eaf4f3}
.service h3{margin-top:20px;font-size:22px;font-weight:500;line-height:30px}
.service p{margin-top:12px;font-size:15.5px;line-height:26px;color:var(--muted)}

/* benefits */
.benefits{top:2104px;left:0;width:1200px;height:507px;background:var(--teal)}
.benefits-photo{left:668px;top:0;width:417px;height:507px;background:linear-gradient(135deg,#d9b48a,#a6532f 35%,#c8c3bd 65%,#eef0f2)}
.benefits .kicker{color:var(--white)}
.benefits-title{font-family:'Cinzel',serif;font-size:42px;color:var(--white)}
.checklist{left:110px;top:190px;width:500px;list-style:none;color:var(--white);font-size:16px}
.checklist li{display:flex;gap:12px;margin-bottom:24px;line-height:24px}
.checklist svg{flex:none;margin-top:4px}

/* testimonials */
.quote-mark{left:193px;top:2772px}
.quote-text{left:225px;top:2812px;width:750px;text-align:center;font-size:19px;line-height:33px;color:#444}
.quote-author{top:2968px;font-size:17px;color:var(--teal)}
.quote-author b{font-weight:600}

/* blog */
.blog{top:3055px;left:0;width:1200px;height:700px;background:var(--soft)}
.card{top:198px;width:307px;height:414px;background:var(--white);box-shadow:0 1px 4px rgba(0,0,0,.08)}
.card-img{height:217px;position:relative}
.date{position:absolute;left:0;top:0;background:var(--teal);color:var(--white);padding:6px 10px;font-size:13px;font-weight:500;line-height:20px}
.date b{display:block;font-size:19px;font-weight:500}
.card h3{margin:22px 22px 0;font-size:21px;font-weight:500}
.card p{margin:14px 22px 0;font-size:15.5px;line-height:25px;color:var(--muted)}
.card a{display:block;margin:16px 22px 0;font-size:17px;font-weight:600;color:var(--teal);text-decoration:none;letter-spacing:.5px}

/* footer */
.footer{top:3700px;left:0;width:1200px;height:654px}
.footer-shape{position:absolute;left:0;top:0}
.footer-brand{left:110px;top:280px;width:245px;height:245px;border-radius:50%;border:2px solid #ddd;display:flex;align-items:center;justify-content:center}
.footer-brand span{font-family:'Cinzel',serif;font-size:30px;color:#ddd;text-align:center;line-height:1.2}
.footer h4{font-size:16px;font-weight:600;color:var(--white);letter-spacing:.5px}
.links{left:497px;top:290px}
.links ul{list-style:none;margin-top:18px}
.links li{font-size:16px;color:#ddd;line-height:29px}
.contact{left:705px;top:290px;color:#ddd;font-size:16px}
.contact .row{display:flex;gap:12px;line-height:28px;margin-top:18px}
.contact svg{flex:none;margin-top:7px}
.rule{left:110px;top:558px;width:980px;height:1px;background:#666}
.copyright{left:110px;top:594px;font-size:16px;color:#ddd}
.social{top:584px;width:44px;height:44px;border-radius:50%;border:2px solid #ddd}
</style>
</head>
<body>

<header class="site-header abs">
  <nav class="nav abs">
    <span class="active">HOME</span><span>ABOUT</span><span>SERVICES</span><span>TESTIMONIALS</span><span>BLOG</span><span>CONTACT</span>
  </nav>
</header>
<div class="brand abs"><span>Rising Paths</span></div>

<section class="hero abs">
  <div class="hero-photo" role="img" aria-label="Hand touching tall grass in a sunlit field"></div>
  <p class="hero-sub abs">Life Coaching</p>
  <h1 class="hero-title abs">RISING PATHS</h1>
  <div class="btn-outline abs">SCHEDULE AN APPOINTMENT</div>
  <svg class="hero-wave" width="1200" height="722" viewBox="0 0 1200 722" aria-hidden="true">
    <path d="M0,672 C120,760 330,760 520,660 C650,590 760,530 900,565 C1020,595 1120,680 1200,722 L1200,722 L0,722 Z" fill="#fff"/>
  </svg>
</section>

<section class="about">
  <div class="about-frame2 abs"></div>
  <div class="about-frame abs"></div>
  <div class="about-photo abs" role="img" aria-label="Portrait of the coach holding a teal mug"></div>
  <div class="about-text abs">
    <p class="kicker">About Me</p>
    <h2 class="about-name">CLARA WHITFIELD</h2>
    <p>Nemo enim ipsam voluptatem quia voluptas sit pern atur aut odit aut fugit, sed quia consequuntur magni dolores eos qui ratione voluptatem sequi nesciuntue porro quisquam est, qui dolorem ipsum quia dolor sit amet, consectetur, adipisci velit.</p>
  </div>
  <div class="signature abs" role="img" aria-label="Handwritten signature of Clara Whitfield"></div>
</section>

<section class="services abs">
  <p class="kicker abs center" style="top:56px">Work With Me</p>
  <h2 class="section-title abs center" style="top:98px">SERVICES</h2>
  <div class="service abs" style="left:98px">
    <div class="service-ring"><div class="service-icon" role="img" aria-label="Employee engagement icon"></div></div>
    <h3>Employee<br>Engagement</h3>
    <p>Duis aute irure dolor in reprehenderit in voluptate velit esse cilludol.</p>
  </div>
  <div class="service abs" style="left:353px">
    <div class="service-ring"><div class="service-icon" role="img" aria-label="Leadership development icon"></div></div>
    <h3>Leadership<br>Development</h3>
    <p>Duis aute irure dolor in reprehenderit in voluptate velit esse cilludol.</p>
  </div>
  <div class="service abs" style="left:607px">
    <div class="service-ring"><div class="service-icon" role="img" aria-label="Executive coaching icon"></div></div>
    <h3>Executive<br>Coaching</h3>
    <p>Duis aute irure dolor in reprehenderit in voluptate velit esse cilludol.</p>
  </div>
  <div class="service abs" style="left:860px">
    <div class="service-ring"><div class="service-icon" role="img" aria-label="Employee assistance icon"></div></div>
    <h3>Employee<br>Assistance</h3>
    <p>Duis aute irure dolor in reprehenderit in voluptate velit esse cilludol.</p>
  </div>
</section>

<section class="benefits abs">
  <div class="abs" style="left:114px;top:66px">
    <p class="kicker">Benefits</p>
    <h2 class="benefits-title">WHY AM I?</h2>
  </div>
  <ul class="checklist abs">
    <li><svg width="16" height="16" viewBox="0 0 16 16"><circle cx="8" cy="8" r="8" fill="#fff"/><path d="M4.5 8.2l2.3 2.3 4.7-4.8" stroke="#00a596" stroke-width="2" fill="none"/></svg>Creating permanent Positive changes to your life.</li>
    <li><svg width="16" height="16" viewBox="0 0 16 16"><circle cx="8" cy="8" r="8" fill="#fff"/><path d="M4.5 8.2l2.3 2.3 4.7-4.8" stroke="#00a596" stroke-width="2" fill="none"/></svg>Nemo enim ipsam voluptatem quia voluptas sit asper.</li>
    <li><svg width="16" height="16" viewBox="0 0 16 16"><circle cx="8" cy="8" r="8" fill="#fff"/><path d="M4.5 8.2l2.3 2.3 4.7-4.8" stroke="#00a596" stroke-width="2" fill="none"/></svg>Satur aut odit aut fugit, sed quia consequuntur mag.</li>
    <li><svg width="16" height="16" viewBox="0 0 16 16"><circle cx="8" cy="8" r="8" fill="#fff"/><path d="M4.5 8.2l2.3 2.3 4.7-4.8" stroke="#00a596" stroke-width="2" fill="none"/></svg>Hi dolores eos qui ratione voluptatem sequi nesciunt.</li>
    <li><svg width="16" height="16" viewBox="0 0 16 16"><circle cx="8" cy="8" r="8" fill="#fff"/><path d="M4.5 8.2l2.3 2.3 4.7-4.8" stroke="#00a596" stroke-width="2" fill="none"/></svg>Neque porro quisquam est, qui dolorem ipsum quia dolor sit amet, consectetur.</li>
  </ul>
  <div class="benefits-photo abs" role="img" aria-label="Two colleagues smiling at a laptop"></div>
</section>

<section class="testimonials">
  <p class="kicker abs center" style="top:2680px">Reviews</p>
  <h2 class="section-title abs center" style="top:2722px">TESTIMONIALS</h2>
  <svg class="quote-mark abs" width="86" height="76" viewBox="0 0 86 76" aria-hidden="true">
    <path d="M22 0h16L26 50c0 14-8 24-16 24S0 66 0 56c0-8 5-12 10-14z" fill="#00a596"/>
    <path d="M68 0h16L72 50c0 14-8 24-16 24s-10-8-10-18c0-8 5-12 10-14z" fill="#00a596"/>
  </svg>
  <p class="quote-text abs">Ut enim ad minima veniam, quis nostrum exercitationem ullam corporis susc ipit laboriosam, nisi ut aliquid ex ea commodi consequatur. Quis autem vel eum iure reprehenderit qui in ea voluptate velit esse quam nihil molesti ae coliq nsequatur, vel illum qui dolorem eum fugiat quo.</p>
  <p class="quote-author abs center">– <b>Mark Ellison</b>, HR Director, Harbor Lane School</p>
</section>

<section class="blog abs">
  <p class="kicker abs center" style="top:67px">Latest Post</p>
  <h2 class="section-title abs center" style="top:110px">BLOG</h2>
  <article class="card abs" style="left:110px">
    <div class="card-img" role="img" aria-label="Letter tiles spelling life skills on wood" style="background:linear-gradient(135deg,#6f6a62,#b9b2a6 50%,#7d7466)"><div class="date">Jul 25<b>2022</b></div></div>
    <h3>Finibus Bonoruet Malo</h3>
    <p>Nemo enim ipsam voluptatem quia voluptas sit aspernatur aut odit aut fugited qui.</p>
    <a>READ MORE</a>
  </article>
  <article class="card abs" style="left:446px">
    <div class="card-img" role="img" aria-label="Chalkboard with steps to success" style="background:linear-gradient(135deg,#1f3a38,#2e4f4c 60%,#3c5c58)"><div class="date">Jul 25<b>2022</b></div></div>
    <h3>Finibus Bonoruet Malo</h3>
    <p>Nemo enim ipsam voluptatem quia voluptas sit aspernatur aut odit aut fugited qui.</p>
    <a>READ MORE</a>
  </article>
  <article class="card abs" style="left:781px">
    <div class="card-img" role="img" aria-label="Team joining raised hands together" style="background:linear-gradient(135deg,#e9e4df,#c88c6c 45%,#9b4c3a 75%,#d8d2cc)"><div class="date">Jul 25<b>2022</b></div></div>
    <h3>Finibus Bonoruet Malo</h3>
    <p>Nemo enim ipsam voluptatem quia voluptas sit aspernatur aut odit aut fugited qui.</p>
    <a>READ MORE</a>
  </article>
</section>

<footer class="footer abs">
  <svg class="footer-shape" width="1200" height="654" viewBox="0 0 1200 654" aria-hidden="true">
    <path d="M0,18 C180,190 400,270 620,210 C840,150 1000,0 1200,20 L1200,654 L0,654 Z" fill="#3e3e40"/>
  </svg>
  <div class="footer-brand abs"><span>Rising Paths</span></div>
  <div class="links abs">
    <h4>QUICK LINKS</h4>
    <ul><li>Home</li><li>About</li><li>Services</li><li>Testimonials</li><li>Blog</li><li>Contact</li></ul>
  </div>
  <div class="contact abs">
    <h4>CONTACT INFORMATION</h4>
    <div class="row"><svg width="12" height="16" viewBox="0 0 12 16"><path d="M6 0C2.7 0 0 2.6 0 5.9 0 10 6 16 6 16s6-6 6-10.1C12 2.6 9.3 0 6 0zm0 8.2A2.3 2.3 0 1 1 6 3.6a2.3 2.3 0 0 1 0 4.6z" fill="#ddd"/></svg><span>2450 Alder Lane, Brookfield,<br>WI 00000</span></div>
    <div class="row" style="margin-top:34px"><svg width="14" height="14" viewBox="0 0 14 14"><path d="M3 0l2.2 3.2-1.4 1.6c.8 1.8 2.2 3.2 4 4l1.6-1.4L14 11l-1.6 2.6C6.5 13.6.4 7.5.4 1.6z" fill="#ddd"/></svg><span>1 555 010 2040</span></div>
    <div class="row" style="margin-top:34px"><svg width="16" height="12" viewBox="0 0 16 12"><rect width="16" height="12" rx="1" fill="#ddd"/><path d="M0 1l8 6 8-6" stroke="#3e3e40" stroke-width="1.5" fill="none"/></svg><span>info@risingpaths.com</span></div>
  </div>
  <div class="rule abs"></div>
  <p class="copyright abs">Copyright © 2022, Rising Paths Coaching. All rights reserved.</p>
  <div class="social abs" style="left:938px"></div>
  <div class="social abs" style="left:990px"></div>
  <div class="social abs" style="left:1043px"></div>
</footer>

</body>
</html>
```